Calloway Brewhouse Beer Can Design

Design a beer can for a boutique craft brewery located in Frankston, Victoria, AUS.
We have a focus on producing socially approachable beers in an ambient setting. The beer can design should be sophisticated, simple, recognizable and a little playful. The color pallet should be inviting and not too bold. The design should have identifying features that can be interchanged onto different cans for different beer types. The design must be repeatable for other beer varieties, which will each have a unique color. The can should feature black, white and purple (this should be in interchangeable color). The beer can also needs to have our Calloway Brewhouse company logo on it, this has been attached to the design brief.

Target Market(s)

The target market is aged 25+ who are social, have some disposable income and appreciate good beer, wine and food.
The beers will also be made for distribution, initially to locally to restaurants and cafés and eventually commercially.
Tourists will also be targeted due to the area the brewhouse is located (Mornington Peninsula, Victoria, AUS).

Industry/Entity Type

Hospitality

Font styles to use
Sans Serif
Script

Colors
6b449b
876aae
b7a5cd
e4daeb
000000
ffffff
959595

Requirements
Must have
• The ‘Calloway Brewhouse’ logo.
• The colour associated to this beer - purple. This should be the only colour used on the can (along with black/white/gray).
• The company tagline ‘Socially Approachable’.
• The tasting notes text ‘Bright in colour, dry on the palate and thirst quenching in the extreme, wheat and pale malts compliment each other with nuance.’
• Australian beer can requirements as per 'Requirements.png'. EPS and AI files of the requirements have been included.
Nice to have
• The logo text ‘Wendel Malt IPA’ more predominant than the Calloway Brewhouse logo.
Should not have
• Be busy, simple is best
• Beer related pictures / images
• Bold, masculine lines and fonts
• Requirements.png directly used. Please use the EPS or AI files provided.

```html
<!DOCTYPE html>
<html lang="en">
<head>
<meta charset="utf-8">
<title>Calloway Brewhouse – Wendel Malt IPA can label</title>
<link rel="stylesheet" href="https://fonts.googleapis.com/css2?family=Barlow+Condensed:ital,wght@0,300;0,400;0,600;0,700;1,300&display=swap">
<style>
  :root {
    --purple-deep: #6b449b;
    --purple: #876aae;
    --purple-soft: #b7a5cd;
    --purple-mist: #e4daeb;
    --ink: #000000;
    --paper: #ffffff;
    --grey: #959595;
    --frame: #c8c8c8;
  }
  html, body {
    margin: 0;
    padding: 0;
    width: 1200px;
    height: 956px;
    overflow: hidden;
    background: var(--paper);
  }
  .label {
    position: relative;
    width: 1194px;
    height: 956px;
    margin-left: 3px;
    box-sizing: border-box;
    border: 1px solid var(--frame);
    background: var(--paper);
    font-family: "Barlow Condensed", "Arial Narrow", sans-serif;
    color: var(--ink);
    overflow: hidden;
  }
  .product-name {
    position: absolute;
    left: 70px;
    top: 128px;
    margin: 0;
    font-weight: 300;
    font-size: 150px;
    line-height: 150px;
    letter-spacing: 2px;
    color: var(--ink);
  }
  .product-name .line { display: block; }
  .product-name .line-two { padding-left: 36px; }
  .product-dot {
    position: absolute;
    left: 446px;
    top: 268px;
    width: 12px;
    height: 12px;
    border-radius: 50%;
    background: var(--purple);
  }
  .product-style {
    position: absolute;
    left: 318px;
    top: 448px;
    margin: 0;
    font-weight: 400;
    font-size: 112px;
    line-height: 112px;
    letter-spacing: 10px;
    color: var(--grey);
  }
  .tasting-notes {
    position: absolute;
    right: 400px;
    top: 416px;
    margin: 0;
    text-align: right;
    font-weight: 300;
    font-style: italic;
    font-size: 16.5px;
    line-height: 19.5px;
    color: var(--purple);
  }
  .abv {
    position: absolute;
    right: 402px;
    top: 542px;
    margin: 0;
    font-weight: 300;
    font-size: 16px;
    color: var(--grey);
  }
  .accent-band {
    position: absolute;
    left: 213px;
    top: 636px;
    width: 564px;
    height: 48px;
    background: var(--purple);
  }
  .brewery-name {
    position: absolute;
    left: 184px;
    top: 842px;
    margin: 0;
    font-weight: 400;
    font-size: 22px;
    letter-spacing: 5px;
    color: var(--ink);
  }
  .brewery-address {
    position: absolute;
    right: 404px;
    top: 838px;
    margin: 0;
    text-align: right;
    font-weight: 400;
    font-size: 16px;
    line-height: 18.5px;
    color: var(--ink);
  }
  .compliance {
    position: absolute;
    left: 0;
    top: 0;
    width: 1200px;
    height: 956px;
    pointer-events: none;
  }
  .compliance text { font-family: "Barlow Condensed", "Arial Narrow", sans-serif; fill: var(--ink); }
  .compliance .small { font-size: 9.5px; font-weight: 600; }
  .compliance .tiny { font-size: 7.5px; font-weight: 400; }
  .compliance .web { font-size: 17px; font-weight: 700; }
  .compliance .deposit { font-size: 32px; font-weight: 700; }
  .compliance .volume { font-size: 13px; font-weight: 600; }
  .compliance .drinks-count { font-size: 18px; font-weight: 700; fill: var(--paper); }
  .compliance .drinks-label { font-size: 11px; font-weight: 700; }
</style>
</head>
<body>
<main class="label">
  <h1 class="product-name">
    <span class="line line-one">Wendel</span>
    <span class="line line-two">Malt</span>
  </h1>
  <span class="product-dot" aria-hidden="true"></span>
  <p class="product-style">IPA</p>

  <p class="tasting-notes">
    Bright in colour,<br>
    dry on the palate and<br>
    thirst quenching in the extreme,<br>
    wheat and pale malts<br>
    compliment each other with nuance.
  </p>
  <p class="abv">4.8 % ABV</p>

  <div class="accent-band" role="img" aria-label="Purple painted accent stroke in the beer's signature colour"></div>

  <p class="brewery-name">CALLOWAY BREWHOUSE</p>

  <p class="brewery-address">
    Brewed &amp; canned<br>
    24 Harbour Lane Seabrook<br>
    MADE IN AUSTRALIA
  </p>

  <svg class="compliance" viewBox="0 0 1200 956" aria-label="Packaging compliance marks">
    <g class="recycle-icon" fill="none" stroke="var(--ink)" stroke-width="11" stroke-linecap="butt">
      <path d="M1013 152 L1048 172"/>
      <path d="M1052 198 L1048 226 L1020 226"/>
      <path d="M998 232 L972 212 L976 190"/>
      <path d="M986 166 L1000 154"/>
    </g>
    <g fill="var(--ink)">
      <path d="M1042 184 L1058 184 L1050 196 Z"/>
      <path d="M1008 216 L1008 236 L996 226 Z"/>
      <path d="M972 176 L990 170 L986 186 Z"/>
    </g>

    <g class="standard-drinks">
      <path d="M935 289 L970 289 C978 292 984 296 990 296 L1026 296 L1026 331 L990 331 C984 331 978 335 970 337 L935 337 Z" fill="var(--ink)"/>
      <rect x="940" y="294" width="3" height="38" fill="var(--paper)"/>
      <text class="drinks-count" transform="translate(962 324) rotate(-90)">1.2</text>
      <text class="drinks-label" transform="translate(1028 345) rotate(180)">Standard Drinks</text>
      <text class="volume" transform="translate(1051 330) rotate(-90)">330 ml</text>
    </g>

    <g class="health-message">
      <text class="tiny" transform="translate(966 550) rotate(-90)">It's safest not to drink while pregnant.</text>
      <text class="web" transform="translate(981 550) rotate(-90)">SipSense.org.au</text>
    </g>

    <g class="container-deposit">
      <text class="deposit" transform="translate(1051 552) rotate(-90)">10c</text>
      <text class="small" transform="translate(1022 507) rotate(-90)">10C REFUND AT COLLECTION</text>
      <text class="small" transform="translate(1035 507) rotate(-90)">DEPOTS/POINTS IN PARTICIPATING</text>
      <text class="small" transform="translate(1048 507) rotate(-90)">STATE/TERRITORY OF PURCHASE</text>
    </g>
  </svg>
</main>
</body>
</html>
```